Veltiwell- Comprehensive quality healthcare delivered at your door.

I am looking for brochures to help promote my business. My business name is Veltiwel (see attachment and logo). This is a new health delivery system designed to provide high quality care to elderly in their communities or at home.

See attachements. The logo is already designed.

As far as services provided (see attachment)

Target Market(s)

Elderly patients

Industry/Entity Type

Business

Font styles to use
Serif

Colors

Designer to choose colors to be used in the design.

```html
<!DOCTYPE html>
<html lang="en">
<head>
<meta charset="utf-8">
<title>Veltiwel Brochure</title>
<link href="https://fonts.googleapis.com/css2?family=Marcellus&family=Playfair+Display:wght@700&family=Montserrat:wght@600;800&family=Questrial&display=swap" rel="stylesheet">
<style>
  :root {
    --olive: #3f5419;
    --olive-dark: #344614;
    --orange: #e8961e;
    --white: #ffffff;
    --ink: #3b3b3b;
    --backdrop: #e6e6e6;
    --photo-light: #f1f4f8;
    --photo-mid: #c9d6e6;
    --photo-deep: #5f86b8;
  }
  * { margin: 0; padding: 0; box-sizing: border-box; }
  html, body { width: 738px; height: 1200px; overflow: hidden; background: var(--backdrop); }
  .canvas { position: relative; width: 738px; height: 1200px; }
  .spread { position: absolute; left: 19px; width: 700px; height: 540px; overflow: hidden; box-shadow: 0 6px 18px rgba(0,0,0,.18); }
  .spread--outside { top: 40px; }
  .spread--inside { top: 620px; }
  .spread > svg.artwork { position: absolute; inset: 0; }
  .abs { position: absolute; }

  .brand-name { font-family: "Marcellus", serif; color: var(--white); letter-spacing: 1px; }
  .brand-mark { position: absolute; border-radius: 50%; background: var(--orange); }

  .cover-brand { left: 0; width: 233px; top: 150px; text-align: center; }
  .cover-brand .brand-mark { left: 80px; top: 0; width: 72px; height: 72px; }
  .cover-brand .brand-name { padding-top: 88px; font-size: 30px; }

  .front-brand { left: 467px; width: 233px; top: 14px; text-align: center; }
  .front-brand .brand-mark { left: 96px; top: 0; width: 42px; height: 42px; }
  .front-brand .brand-name { padding-top: 50px; font-size: 19px; }

  .sites { left: 252px; top: 40px; }
  .sites__title { font-family: "Playfair Display", serif; font-weight: 700; font-size: 19px; color: var(--orange); letter-spacing: .5px; }
  .sites__rule { width: 40px; height: 2px; background: var(--orange); margin: 4px 0 6px; }
  .sites__place { font-family: "Questrial", sans-serif; font-size: 15px; color: var(--white); }

  .intro { left: 22px; top: 48px; width: 200px; }
  .intro__title { font-family: "Montserrat", sans-serif; font-weight: 800; font-size: 27px; color: var(--orange); line-height: 1; margin-bottom: 8px; }
  .intro p { font-family: "Questrial", sans-serif; font-size: 8.6px; line-height: 1.35; color: var(--ink); margin-bottom: 6px; }

  .list { list-style: none; font-family: "Questrial", sans-serif; }
  .list li { display: flex; align-items: flex-start; gap: 5px; margin-bottom: 5px; }
  .list svg { flex: none; width: 9px; height: 9px; margin-top: 1px; }
  .list--settings { left: 40px; top: 338px; font-size: 10px; color: var(--orange); }
  .list--settings li { margin-bottom: 5.5px; }
  .list--care { font-size: 9.6px; color: var(--white); line-height: 1.25; }
  .services { left: 252px; top: 352px; width: 200px; }
  .services__title { font-family: "Montserrat", sans-serif; font-weight: 800; font-size: 19px; color: var(--orange); margin-bottom: 6px; }
  .list--more { left: 484px; top: 252px; width: 200px; }

  .badge { left: 340px; top: 200px; width: 84px; height: 84px; border-radius: 50%; background: var(--white); border: 3px solid #d9d9d9; display: flex; align-items: center; justify-content: center; }
  .badge .brand-name { color: var(--olive); font-size: 12px; }
</style>
</head>
<body>
<svg width="0" height="0" style="position:absolute">
  <defs>
    <symbol id="tick" viewBox="0 0 10 10">
      <circle cx="5" cy="5" r="4.2" fill="none" stroke="currentColor" stroke-width="1.1"/>
      <path d="M3 5.1 L4.5 6.5 L7.1 3.7" fill="none" stroke="currentColor" stroke-width="1.2"/>
    </symbol>
  </defs>
</svg>

<main class="canvas">
  <section class="spread spread--outside">
    <svg class="artwork" viewBox="0 0 700 540" width="700" height="540">
      <defs>
        <linearGradient id="teamPhoto" x1="0" y1="0" x2="1" y2="1">
          <stop offset="0" stop-color="var(--photo-light)"/>
          <stop offset=".55" stop-color="var(--photo-mid)"/>
          <stop offset="1" stop-color="var(--photo-deep)"/>
        </linearGradient>
      </defs>
      <rect width="700" height="540" fill="var(--olive)"/>
      <path d="M150 540 C250 330 380 170 700 130 L700 540 Z" fill="url(#teamPhoto)" role="img" aria-label="Photo of a smiling nurse in blue scrubs with a medical team meeting behind her"/>
      <path d="M142 540 C242 326 376 162 700 121" fill="none" stroke="var(--orange)" stroke-width="8"/>
      <line x1="233" y1="0" x2="233" y2="540" stroke="rgba(0,0,0,.12)"/>
      <line x1="467" y1="0" x2="467" y2="540" stroke="rgba(0,0,0,.12)"/>
    </svg>

    <div class="abs cover-brand">
      <span class="brand-mark"></span>
      <div class="brand-name">VELTIWEL</div>
    </div>

    <div class="abs sites">
      <div class="sites__title">SITES OF OPERATIONS</div>
      <div class="sites__rule"></div>
      <div class="sites__place">Still Meadows</div>
    </div>

    <div class="abs front-brand">
      <span class="brand-mark"></span>
      <div class="brand-name">VELTIWEL</div>
    </div>
  </section>

  <section class="spread spread--inside">
    <svg class="artwork" viewBox="0 0 700 540" width="700" height="540">
      <defs>
        <linearGradient id="staffPhoto" x1="0" y1="0" x2="1" y2="0">
          <stop offset="0" stop-color="#f3f3f3"/>
          <stop offset=".5" stop-color="#e4e8ee"/>
          <stop offset="1" stop-color="#eef0f3"/>
        </linearGradient>
        <linearGradient id="carePhoto" x1="0" y1="0" x2="1" y2="1">
          <stop offset="0" stop-color="#dfe7f1"/>
          <stop offset="1" stop-color="#8fa9c9"/>
        </linearGradient>
      </defs>
      <rect width="700" height="540" fill="var(--white)"/>
      <rect x="233" y="0" width="467" height="320" fill="url(#staffPhoto)" role="img" aria-label="Photo of smiling doctors and nurses giving a thumbs up"/>
      <path d="M0 300 Q200 284 350 268 Q520 222 700 165 L700 540 L0 540 Z" fill="var(--olive)"/>
      <path d="M0 300 Q200 284 350 268 Q520 222 700 165" fill="none" stroke="var(--orange)" stroke-width="6"/>
      <line x1="233" y1="0" x2="233" y2="540" stroke="rgba(0,0,0,.1)"/>
      <line x1="467" y1="0" x2="467" y2="540" stroke="rgba(0,0,0,.1)"/>
      <circle cx="300" cy="285" r="62" fill="#f5f5f5" stroke="#d6d6d6" stroke-width="3"/>
      <circle cx="300" cy="285" r="55" fill="url(#carePhoto)" role="img" aria-label="Photo of a caregiver with an elderly woman"/>
    </svg>

    <div class="abs intro">
      <h1 class="intro__title">STAY HOME</h1>
      <p>Veltiwel offers home and Community Based Services for adults who wish to continue to live independently in the comfort of their communities.</p>
      <p>We provide on site services and deliver high quality healthcare at your door. Our experienced physicians coordinate care with our certified nurse practitioners and provide chronic care management, physical therapy, rehabilitation and medications management.</p>
    </div>

    <div class="abs badge"><span class="brand-name">VELTIWEL</span></div>

    <ul class="abs list list--settings">
      <li><svg><use href="#tick"/></svg>Home</li>
      <li><svg><use href="#tick"/></svg>Assisted Living</li>
      <li><svg><use href="#tick"/></svg>Skilled Nursing</li>
      <li><svg><use href="#tick"/></svg>Independent Living</li>
      <li><svg><use href="#tick"/></svg>Home and Community Based Services</li>
      <li><svg><use href="#tick"/></svg>Respite Care</li>
      <li><svg><use href="#tick"/></svg>Rehabilitation</li>
      <li><svg><use href="#tick"/></svg>MINDA Learning</li>
      <li><svg><use href="#tick"/></svg>Center</li>
      <li><svg><use href="#tick"/></svg>MINDA Learning</li>
    </ul>

    <div class="abs services">
      <h2 class="services__title">Services</h2>
      <ul class="list list--care">
        <li><svg><use href="#tick"/></svg>Comprehensive primary care services</li>
        <li><svg><use href="#tick"/></svg>Coordination of speciality care</li>
        <li><svg><use href="#tick"/></svg>Chronic disease management such as COPD, Asthma, Diabetes mellitus,</li>
        <li><svg><use href="#tick"/></svg>Heart disease like congestive heart failure, Alzheimer's dementia, etc...</li>
      </ul>
    </div>

    <ul class="abs list list--care list--more">
      <li><svg><use href="#tick"/></svg>Transitional Care</li>
      <li><svg><use href="#tick"/></svg>Skilled nursing visits for wound care, catheter care, ostomy</li>
      <li><svg><use href="#tick"/></svg>Social services assessment</li>
      <li><svg><use href="#tick"/></svg>Home health assistance</li>
      <li><svg><use href="#tick"/></svg>Physical therapy</li>
      <li><svg><use href="#tick"/></svg>Mental health</li>
      <li><svg><use href="#tick"/></svg>Dental health</li>
      <li><svg><use href="#tick"/></svg>Transportation</li>
    </ul>
  </section>
</main>
</body>
</html>
```